Simple graphic for a book or slide presentation

We are looking for a style that suits the style of our book. It's title is Venture. Thriving boldly on uncertain ground. There will be more line drawing/graphics in the book but how you design this image will create the style for all the other simple graphics in the book (once we decide what they are). So this one design will lead to a few more to match the style of this one. We'd like the shape of the overall graphic (i.e the arrows and words/bubbles) to be circular (not a rounded square as appears in the sample attached). Perhaps the words don't need to be in ovals or bound by anything at all; perhaps they do - let's see what you see. We'd like you to choose a font or offer many different fonts you think will capture the practical yet unconventional tone of the book. The book is teaching that managing risks in life is a life-skill that can be learned. The section of the book where this graphic will be placed is called "the power of language" - basically we are saying that thoughts, words and actions create our culture and our destiny. This insight comes from Pranav Kelkari's famous quote:
Carefully watch your thoughts, for they become your words.
Manage and watch your words, for they will become your actions.
Consider and judge your actions, for they have become your habits.
Acknowledge and watch your habits, for they shall become your values.
Understand and embrace your values, for they become your destiny.

Please change the text in the middle of the graphic to say: The Human Culture Cycle

```html
<!DOCTYPE html>
<html lang="en">
<head>
<meta charset="utf-8">
<title>The Human Culture Cycle</title>
<link rel="stylesheet" href="https://fonts.googleapis.com/css2?family=Roboto:wght@700&display=swap">
<style>
  :root {
    --ink: #333132;
    --paper: #ffffff;
    --frame: #5a5a5a;
  }
  html, body {
    margin: 0;
    padding: 0;
    width: 1200px;
    height: 1200px;
    overflow: hidden;
    background: var(--paper);
  }
  .canvas {
    position: relative;
    width: 1200px;
    height: 1200px;
    box-sizing: border-box;
    border: 1px solid var(--frame);
    background: var(--paper);
  }
  .cycle-diagram {
    display: block;
    width: 1200px;
    height: 1200px;
  }
  .stage-ring,
  .hub-ring {
    fill: var(--paper);
    stroke: var(--ink);
    stroke-width: 14;
  }
  .flow-arrow {
    fill: none;
    stroke: var(--ink);
    stroke-width: 12;
  }
  .arrow-head {
    fill: var(--ink);
  }
  .stage-label,
  .hub-label {
    font-family: "Roboto", Arial, sans-serif;
    font-weight: 700;
    fill: var(--ink);
    text-anchor: middle;
    dominant-baseline: central;
  }
  .stage-label {
    font-size: 26px;
    letter-spacing: 1.5px;
  }
  .hub-label {
    font-size: 27px;
    letter-spacing: 2px;
  }
</style>
</head>
<body>
<main class="canvas">
  <svg class="cycle-diagram" viewBox="0 0 1320 1320" role="img" aria-label="The Human Culture Cycle: culture, thoughts, words, actions, habits, values">
    <defs>
      <marker id="arrowhead" viewBox="0 0 10 10" markerUnits="userSpaceOnUse" markerWidth="38" markerHeight="38" refX="1" refY="5" orient="auto">
        <path class="arrow-head" d="M0 0 L10 5 L0 10 Z"/>
      </marker>
    </defs>

    <g class="flow-arrows">
      <path class="flow-arrow" marker-end="url(#arrowhead)" d="M618.1 395.3 A268 268 0 0 1 655.3 392.0"/>
      <path class="flow-arrow" marker-end="url(#arrowhead)" d="M868.3 491.3 A268 268 0 0 1 889.7 522.0"/>
      <path class="flow-arrow" marker-end="url(#arrowhead)" d="M910.2 756.0 A268 268 0 0 1 894.4 789.9"/>
      <path class="flow-arrow" marker-end="url(#arrowhead)" d="M701.9 924.7 A268 268 0 0 1 664.7 928.0"/>
      <path class="flow-arrow" marker-end="url(#arrowhead)" d="M451.7 828.7 A268 268 0 0 1 430.3 798.0"/>
      <path class="flow-arrow" marker-end="url(#arrowhead)" d="M409.8 564.0 A268 268 0 0 1 425.6 530.1"/>
    </g>

    <g class="stage stage-culture">
      <circle class="stage-ring" cx="526" cy="428" r="90"/>
      <text class="stage-label" x="526" y="428">CULTURE</text>
    </g>
    <g class="stage stage-thoughts">
      <circle class="stage-ring" cx="794" cy="428" r="90"/>
      <text class="stage-label" x="794" y="428">THOUGHTS</text>
    </g>
    <g class="stage stage-words">
      <circle class="stage-ring" cx="928" cy="660" r="90"/>
      <text class="stage-label" x="928" y="660">WORDS</text>
    </g>
    <g class="stage stage-actions">
      <circle class="stage-ring" cx="794" cy="892" r="90"/>
      <text class="stage-label" x="794" y="892">ACTIONS</text>
    </g>
    <g class="stage stage-habits">
      <circle class="stage-ring" cx="526" cy="892" r="90"/>
      <text class="stage-label" x="526" y="892">HABITS</text>
    </g>
    <g class="stage stage-values">
      <circle class="stage-ring" cx="392" cy="660" r="90"/>
      <text class="stage-label" x="392" y="660">VALUES</text>
    </g>

    <g class="hub">
      <circle class="hub-ring" cx="660" cy="660" r="117"/>
      <text class="hub-label" x="660" y="613">THE</text>
      <text class="hub-label" x="660" y="645">HUMAN</text>
      <text class="hub-label" x="660" y="676">CULTURE</text>
      <text class="hub-label" x="660" y="708">CYCLE</text>
    </g>
  </svg>
</main>
</body>
</html>
```